Service business needs Business Card Design

Looking to create a new business card design that is both professional and unique the can highlight the many services we offer throughout the seasons. Our tagline is "The Steadfast Touch"
Licensed & Insured: PA392617 has to be small and on the back side of the card.
On the Front:
FirstName LastName
Title
We offer the following services:
Deck Repair and Maintenance
Deck Cleaning and Staining/Painting
Power Washing/House Washing
Landscape Lighting Installation
Christmas Lighting Installation

```html
<!DOCTYPE html>
<html lang="en">
<head>
<meta charset="utf-8">
<title>Halden Services – Business Card</title>
<link rel="stylesheet" href="https://fonts.googleapis.com/css2?family=Exo+2:wght@400;600;700&family=Roboto:wght@400;500&family=Roboto+Condensed:wght@700&family=Kalam:wght@400&display=swap">
<style>
  :root {
    --backdrop: #2a2a2a;
    --card: #efefef;
    --card-edge: #e2e2e2;
    --navy: #0b4a87;
    --blue: #1d7fbd;
    --sky: #46b6e1;
    --ink: #1d1d1d;
    --white: #ffffff;
  }
  * { box-sizing: border-box; margin: 0; padding: 0; }
  html, body { width: 1200px; height: 1138px; overflow: hidden; }
  body { background: var(--backdrop); position: relative; font-family: "Roboto", sans-serif; }

  .card {
    position: absolute;
    left: 288px;
    width: 624px;
    height: 376px;
    border-radius: 16px;
    background: linear-gradient(180deg, #f4f4f4 0%, var(--card) 60%, var(--card-edge) 100%);
    overflow: hidden;
  }
  .card--back { top: 184px; }
  .card--front { top: 606px; }

  /* back side */
  .brand-lockup {
    position: absolute;
    left: 0; right: 0; top: 92px;
    display: flex; align-items: center; justify-content: center; gap: 16px;
    font-family: "Exo 2", sans-serif; font-weight: 700;
    color: var(--blue);
    font-size: 52px; letter-spacing: 3px;
  }
  .brand-lockup .mark { width: 38px; height: 38px; background: var(--blue); }

  .services-band {
    position: absolute;
    left: 0; right: 0; top: 243px; height: 80px;
    background: linear-gradient(90deg, #1b73ad 0%, #2a93c9 50%, var(--sky) 100%);
    display: flex; flex-direction: column; justify-content: center; align-items: center;
    font-family: "Exo 2", sans-serif; font-size: 16px; line-height: 22.5px;
    color: var(--white);
    padding-left: 20px;
  }
  .services-band .sep { margin: 0 14px; }

  .license {
    position: absolute;
    left: 0; right: 0; top: 335px;
    display: flex; align-items: center; justify-content: center; gap: 28px;
    font-family: "Roboto", sans-serif; font-size: 16.5px; color: var(--navy);
  }
  .license .rule { width: 72px; height: 2px; background: linear-gradient(90deg, transparent, var(--sky) 30%, var(--sky) 70%, transparent); }

  /* front side */
  .brand-stack {
    position: absolute;
    left: 44px; top: 118px; width: 240px;
    display: flex; align-items: center; gap: 12px;
    font-family: "Exo 2", sans-serif; font-weight: 700; color: var(--navy);
    font-size: 30px; line-height: 32px; letter-spacing: 2px;
  }
  .brand-stack .mark { width: 30px; height: 30px; background: var(--navy); flex: none; }

  .contact {
    position: absolute; left: 331px; top: 102px;
  }
  .contact .name {
    font-family: "Roboto Condensed", sans-serif; font-weight: 700;
    font-size: 25px; color: var(--navy); line-height: 28px;
  }
  .contact .title { font-size: 16px; color: var(--ink); margin-top: 2px; }
  .contact ul { list-style: none; margin-top: 23px; }
  .contact li {
    display: flex; align-items: center; gap: 16px;
    font-size: 16px; color: var(--ink); height: 24px;
  }
  .contact svg { width: 16px; height: 16px; fill: var(--blue); flex: none; }

  .foot { position: absolute; left: 0; bottom: 0; width: 100%; height: 47px; }
  .tagline {
    position: absolute; left: 335px; bottom: 10px;
    font-family: "Kalam", cursive; font-size: 19px; color: var(--white);
  }
</style>
</head>
<body>

<section class="card card--back" aria-label="Card back">
  <div class="brand-lockup"><span class="mark"></span>HALDEN</div>
  <div class="services-band">
    <p>Deck Repair and Maintenance<span class="sep">|</span>Deck Cleaning and Staining/Painting</p>
    <p>Power Washing and House Washing</p>
    <p>Landscape Lighting Installation &nbsp;&amp;&nbsp; Christmas Lighting Installation</p>
  </div>
  <div class="license"><span class="rule"></span><span>Licensed &amp; Insured: PA392617</span><span class="rule"></span></div>
</section>

<section class="card card--front" aria-label="Card front">
  <div class="brand-stack"><span class="mark"></span><span>HALDEN<br>SERVICES</span></div>

  <div class="contact">
    <h1 class="name">Marlon Castellane</h1>
    <p class="title">CEO and Owner</p>
    <ul>
      <li>
        <svg viewBox="0 0 16 16" aria-hidden="true"><path d="M1 6c0-2 3-3.5 7-3.5S15 4 15 6v1h-3.5V5.5h-7V7H1z"/><path d="M4 8h8l1.5 6h-11z"/></svg>
        +1 610-555-0183
      </li>
      <li>
        <svg viewBox="0 0 16 16" aria-hidden="true"><path d="M1 3h14v10H1z M2.5 4.5v.4L8 9l5.5-4.1v-.4z" fill-rule="evenodd"/></svg>
        info@haldenservicesgroup.com
      </li>
      <li>
        <svg viewBox="0 0 16 16" aria-hidden="true"><circle cx="8" cy="8" r="7"/><path d="M1 8h14M8 1v14M3 4.5h10M3 11.5h10" stroke="#efefef" stroke-width="1" fill="none"/><ellipse cx="8" cy="8" rx="3" ry="7" stroke="#efefef" stroke-width="1" fill="none"/></svg>
        www.haldenservicesgroup.com
      </li>
    </ul>
  </div>

  <svg class="foot" viewBox="0 0 624 47" preserveAspectRatio="none" aria-hidden="true">
    <rect x="0" y="32" width="290" height="15" fill="var(--sky)"/>
    <path d="M290 0 H624 V47 H264 L272 32 L290 0 Z" fill="var(--navy)"/>
  </svg>
  <p class="tagline">The Steadfast Touch</p>
</section>

</body>
</html>
```